Email Banner Ad for Tidewell Power company

We are looking for an Email Banner Ad for all emails which is link to website

Regarding MEES compliance coming in April 2018

All the details can be found on our website www.brindlequay.co.uk

Our current footer is attached from last year and we are looking for a new one

Target Market(s)

Property companies and investor

Industry/Entity Type

It Company

Requirements
Must have
• a link to website
• must be the size to go at the bottom of emails
Nice to have
• similar to website
• similar to the advertisement we have had done already

```html
<!DOCTYPE html>
<html lang="en">
<head>
<meta charset="utf-8">
<title>Tidewell Power – Email Banner</title>
<link rel="stylesheet" href="https://fonts.googleapis.com/css2?family=Roboto+Condensed:wght@400;700&display=swap">
<style>
  :root {
    --page-bg: #282828;
    --panel-white: #ffffff;
    --ink-dark: #3b3b3b;
    --green-deep: #1c7443;
    --green-bright: #3cb44b;
    --lime: #9be03c;
    --bolt-red: #f15a40;
    --text-light: #ffffff;
    --accent-dot: #3cb44b;
  }
  html, body {
    margin: 0;
    width: 1200px;
    height: 1200px;
    overflow: hidden;
    background: var(--page-bg);
  }
  .email-banner {
    position: absolute;
    left: 145px;
    top: 544px;
    width: 910px;
    height: 112px;
    display: block;
    text-decoration: none;
    box-shadow: 3px 4px 6px rgba(0, 0, 0, 0.55);
    font-family: "Roboto Condensed", sans-serif;
  }
  .banner-art {
    position: absolute;
    inset: 0;
    width: 910px;
    height: 112px;
  }
  .brand-panel {
    position: absolute;
    left: 0;
    top: 0;
    width: 244px;
    height: 112px;
    display: flex;
    align-items: center;
    justify-content: center;
    gap: 8px;
  }
  .brand-dot {
    width: 14px;
    height: 14px;
    border-radius: 50%;
    background: var(--accent-dot);
  }
  .brand-name {
    font-weight: 700;
    font-size: 29px;
    color: var(--ink-dark);
    letter-spacing: 0.2px;
  }
  .campaign-mark {
    position: absolute;
    left: 258px;
    top: 0;
    width: 96px;
    height: 112px;
    display: flex;
    align-items: center;
    justify-content: center;
    font-weight: 700;
    font-size: 25px;
    color: var(--text-light);
  }
  .divider {
    position: absolute;
    left: 361px;
    top: 20px;
    width: 1px;
    height: 74px;
    background: var(--text-light);
  }
  .headline {
    position: absolute;
    left: 372px;
    top: 17px;
    margin: 0;
    font-weight: 400;
    font-size: 21px;
    line-height: 26px;
    color: var(--text-light);
  }
  .headline .date {
    font-weight: 700;
    color: var(--lime);
  }
</style>
</head>
<body>
  <a class="email-banner" href="https://www.brindlequay.co.uk" aria-label="Tidewell Power – visit www.brindlequay.co.uk">
    <svg class="banner-art" viewBox="0 0 910 112" aria-hidden="true">
      <defs>
        <linearGradient id="green-field" x1="0" y1="0" x2="1" y2="0">
          <stop offset="0" stop-color="var(--green-deep)"/>
          <stop offset="1" stop-color="var(--green-bright)"/>
        </linearGradient>
        <linearGradient id="city-tones" x1="0" y1="0" x2="1" y2="0">
          <stop offset="0" stop-color="#8e9193"/>
          <stop offset="0.35" stop-color="#4e5153"/>
          <stop offset="0.6" stop-color="#c9cbcc"/>
          <stop offset="1" stop-color="#9a9795"/>
        </linearGradient>
      </defs>
      <rect x="0" y="0" width="244" height="112" fill="var(--panel-white)"/>
      <rect x="650" y="0" width="260" height="112" fill="url(#city-tones)"/>
      <polygon points="244,0 712,0 664,112 244,112" fill="url(#green-field)"/>
      <polygon points="712,0 734,0 706,50 724,52 662,112 684,62 668,60" fill="var(--bolt-red)"/>
    </svg>
    <span role="img" aria-label="Photograph of city office towers" style="position:absolute;left:740px;top:0;width:170px;height:112px;"></span>

    <div class="brand-panel">
      <span class="brand-dot"></span>
      <span class="brand-name">Tidewell Power</span>
    </div>

    <div class="campaign-mark">Tidewell</div>
    <span class="divider"></span>

    <p class="headline">
      Minimum Energy Performance<br>
      Standards (MEPS)<br>
      England, <span class="date">April&nbsp; 2018</span>
    </p>
  </a>
</body>
</html>
```